Lantern Signs Facebook Banner Design

Design a facebook banner for a sign company. I would like to have a modern approach to it.

Product Offering:
Signs
Banners
Decals
Commercial Wraps

```html
<!DOCTYPE html>
<html lang="en">
<head>
<meta charset="UTF-8">
<title>Lantern Signs – Cover Banner</title>
<link rel="stylesheet" href="https://fonts.googleapis.com/css2?family=Poppins:wght@400;800&display=swap">
<style>
  :root {
    --bg-top: #fdf6f4;
    --bg-bottom: #fcebe6;
    --brand-red: #e8343a;
    --ink: #2f2f33;
    --splash-cyan: #22c4f0;
    --splash-cyan-light: #6fdcfb;
    --splash-pink: #e8197d;
    --splash-purple: #8a1fd6;
    --bottle-blue: #1f3f8f;
    --bottle-light: #3566c4;
    --mug-white: #f7f7f7;
    --mug-shade: #d9d9d9;
  }
  * { margin: 0; padding: 0; box-sizing: border-box; }
  html, body { width: 1200px; height: 445px; overflow: hidden; }
  body { font-family: "Poppins", sans-serif; }

  .banner {
    position: relative;
    width: 1200px;
    height: 445px;
    overflow: hidden;
    background: linear-gradient(180deg, var(--bg-top), var(--bg-bottom));
  }

  .splash { position: absolute; }
  .splash--left {
    left: 0; top: 100px; width: 200px; height: 345px;
    background: linear-gradient(160deg, var(--splash-cyan-light), var(--splash-cyan));
    border-radius: 0 60% 0 0 / 0 40% 0 0;
  }
  .splash--right {
    right: 0; top: 0; width: 140px; height: 424px;
    background: linear-gradient(180deg, var(--splash-pink), var(--splash-purple));
    border-radius: 70% 0 0 60% / 30% 0 0 40%;
    opacity: 0.9;
  }

  .product { position: absolute; }
  .product--bottle {
    left: 150px; top: 45px; width: 100px; height: 375px;
    border-radius: 40px 40px 30px 30px;
    background: linear-gradient(90deg, var(--bottle-blue), var(--bottle-light) 45%, var(--bottle-blue));
    transform: rotate(-18deg);
    box-shadow: 0 18px 30px rgba(0,0,0,0.18);
  }
  .product--mug {
    left: 855px; top: 100px; width: 265px; height: 270px;
    background: radial-gradient(circle at 40% 40%, var(--mug-white), var(--mug-shade));
    border-radius: 20px 70px 70px 20px;
    box-shadow: 0 16px 28px rgba(0,0,0,0.12);
  }

  .brand {
    position: absolute;
    left: 0; right: 0; top: 68px;
    text-align: center;
    color: var(--brand-red);
    font-weight: 800;
    text-transform: uppercase;
    line-height: 1;
  }
  .brand__line { display: block; font-size: 54px; letter-spacing: 1px; }
  .brand__line + .brand__line { margin-top: 2px; }

  .services {
    position: absolute;
    left: 0; right: 0; top: 194px;
    list-style: none;
    text-align: center;
  }
  .services__item {
    display: flex;
    align-items: center;
    justify-content: center;
    gap: 10px;
    height: 44px;
    font-size: 24px;
    font-weight: 400;
    color: var(--ink);
  }
  .services__icon { width: 26px; height: 30px; flex: none; }
</style>
</head>
<body>
  <main class="banner">
    <div class="splash splash--left" role="img" aria-label="Cyan paint splash"></div>
    <div class="splash splash--right" role="img" aria-label="Pink and purple paint splash"></div>

    <div class="product product--bottle" role="img" aria-label="Blue water bottle printed with the Lantern Signs name"></div>
    <div class="product product--mug" role="img" aria-label="White mug printed with the Lantern Signs name"></div>

    <h1 class="brand">
      <span class="brand__line">Lantern</span>
      <span class="brand__line">Signs</span>
    </h1>

    <ul class="services">
      <li class="services__item">
        <svg class="services__icon" viewBox="0 0 26 30" aria-hidden="true">
          <rect x="2" y="2" width="18" height="9" rx="2" fill="var(--brand-red)"/>
          <path d="M20 6h3v7H12v5" fill="none" stroke="var(--ink)" stroke-width="2"/>
          <rect x="10" y="18" width="4" height="10" rx="1.5" fill="var(--ink)"/>
        </svg>Signs
      </li>
      <li class="services__item">
        <svg class="services__icon" viewBox="0 0 26 30" aria-hidden="true">
          <rect x="2" y="2" width="18" height="9" rx="2" fill="var(--brand-red)"/>
          <path d="M20 6h3v7H12v5" fill="none" stroke="var(--ink)" stroke-width="2"/>
          <rect x="10" y="18" width="4" height="10" rx="1.5" fill="var(--ink)"/>
        </svg>Banners
      </li>
      <li class="services__item">
        <svg class="services__icon" viewBox="0 0 26 30" aria-hidden="true">
          <rect x="2" y="2" width="18" height="9" rx="2" fill="var(--brand-red)"/>
          <path d="M20 6h3v7H12v5" fill="none" stroke="var(--ink)" stroke-width="2"/>
          <rect x="10" y="18" width="4" height="10" rx="1.5" fill="var(--ink)"/>
        </svg>Decals
      </li>
      <li class="services__item">
        <svg class="services__icon" viewBox="0 0 26 30" aria-hidden="true">
          <rect x="2" y="2" width="18" height="9" rx="2" fill="var(--brand-red)"/>
          <path d="M20 6h3v7H12v5" fill="none" stroke="var(--ink)" stroke-width="2"/>
          <rect x="10" y="18" width="4" height="10" rx="1.5" fill="var(--ink)"/>
        </svg>Commercial Wraps
      </li>
    </ul>
  </main>
</body>
</html>
```